Need UI design for an iOS app game with most of the layout planned

The name of the game is "QUADRIX".

The goal of the game is to find a way to manipulate four numbers so that the end result is 24. Addition, subtraction, multiplication and division may be used and each number can only be used once.

The list of items we need is:

1. launch image, app icon, UI design of all scenes (10-12 scenes) of the app.
2. App background image should support screen size of both 640x1136.
3. Files are preferred to be in (.eps) format so that resolution can be adjusted later. But other file formats are welcome as long as resolution is high enough.
4. Icons, buttons, background image etc. should have their own file so that later they can be moved around in case design is changed.

The detailed requirement is in the attached file. The actual layout can vary if it can help achieve better result. We also attached several screenshots from iOS game "Glimtor". You can use that as your reference.

```html
<!DOCTYPE html>
<html lang="en">
<head>
<meta charset="utf-8">
<title>QUADRIX – Home Screen</title>
<link href="https://fonts.googleapis.com/css2?family=Nunito:wght@900&family=Inter:wght@600&display=swap" rel="stylesheet">
<style>
  :root {
    --page-bg: #8fdcf0;
    --screen-deep: #2457a3;
    --screen-mid: #2c74c4;
    --screen-light: #1f86d6;
    --screen-light-edge: #0f6fc0;
    --status-bg: #0a1a2c;
    --status-text: #e8eef5;
    --icon-circle: #4bb3ea;
    --icon-circle-soft: #3a9be0;
    --white: #ffffff;
    --btn-yellow-top: #ffc21a;
    --btn-yellow-bottom: #ffa800;
    --btn-orange-top: #ff8a12;
    --btn-orange-bottom: #ff6a00;
    --logo-orange: #ff7a0c;
  }
  html, body {
    margin: 0;
    padding: 0;
    width: 1200px;
    height: 1200px;
    overflow: hidden;
    background: var(--page-bg);
  }
  .canvas {
    position: relative;
    width: 1200px;
    height: 1200px;
    background: linear-gradient(180deg, #b4e6f7 0%, #8fdcf0 55%, #5ec2dc 100%);
  }
  .screen {
    position: absolute;
    top: 225px;
    width: 420px;
    height: 749px;
    overflow: hidden;
    box-shadow: 0 18px 40px rgba(10, 60, 100, 0.25);
  }
  .screen--classic { left: 150px; background: linear-gradient(180deg, var(--screen-mid) 0%, var(--screen-deep) 70%); }
  .screen--bright { left: 630px; background: linear-gradient(180deg, var(--screen-light) 0%, var(--screen-light-edge) 100%); }

  .status-bar {
    position: absolute;
    top: 0; left: 0; right: 0;
    height: 28px;
    background: var(--status-bg);
    display: flex;
    align-items: center;
    padding: 0 10px;
    box-sizing: border-box;
    font-family: "Inter", sans-serif;
    font-weight: 600;
    font-size: 16px;
    color: var(--status-text);
  }
  .status-bar .carrier { display: flex; align-items: center; gap: 4px; }
  .status-bar .lock { position: absolute; left: 50%; transform: translateX(-50%); top: 6px; }
  .status-bar .battery { margin-left: auto; }

  .round-icon {
    position: absolute;
    top: 44px;
    width: 78px;
    height: 78px;
    border-radius: 50%;
    background: var(--icon-circle);
    display: flex;
    align-items: center;
    justify-content: center;
  }
  .screen--bright .round-icon { background: var(--icon-circle-soft); }
  .round-icon--settings { left: 20px; }
  .round-icon--info { right: 20px; }

  .burst {
    position: absolute;
    left: 33px;
    top: 60px;
    width: 360px;
    height: 360px;
    border-radius: 50%;
    background: radial-gradient(circle, rgba(255,255,255,0.35) 0%, rgba(255,255,255,0.12) 45%, rgba(255,255,255,0) 70%);
  }
  .brand {
    position: absolute;
    left: 0; right: 0;
    top: 212px;
    display: flex;
    justify-content: center;
    align-items: center;
    gap: 10px;
    font-family: "Nunito", sans-serif;
    font-weight: 900;
    font-size: 40px;
    color: var(--white);
    letter-spacing: 1px;
  }
  .brand .mark {
    width: 30px;
    height: 30px;
    border-radius: 6px;
    background: var(--logo-orange);
  }

  .menu-button {
    position: absolute;
    left: 56px;
    width: 300px;
    height: 76px;
    border-radius: 7px;
    display: flex;
    align-items: center;
    justify-content: center;
    font-family: "Nunito", sans-serif;
    font-weight: 900;
    font-size: 27px;
    color: var(--white);
    text-shadow: 0 1px 2px rgba(120, 60, 0, 0.35);
  }
  .menu-button--single { top: 490px; background: linear-gradient(180deg, var(--btn-yellow-top), var(--btn-yellow-bottom)); }
  .menu-button--multi { top: 594px; background: linear-gradient(180deg, var(--btn-orange-top), var(--btn-orange-bottom)); }
  .screen--bright .menu-button { left: 64px; width: 296px; }
</style>
</head>
<body>
<main class="canvas">

  <section class="screen screen--classic" aria-label="Home screen, classic blue theme">
    <div class="status-bar">
      <span class="carrier">
        <svg width="18" height="12" viewBox="0 0 18 12"><rect x="0" y="9" width="3" height="3" fill="#e8eef5"/><rect x="4" y="7" width="3" height="5" fill="#e8eef5"/><rect x="8" y="5" width="3" height="7" fill="#e8eef5"/><rect x="12" y="2" width="3" height="10" fill="#e8eef5"/></svg>
        CARRIER
      </span>
      <svg class="lock" width="12" height="16" viewBox="0 0 12 16"><path d="M3 7V4.5a3 3 0 0 1 6 0V7" fill="none" stroke="#e8eef5" stroke-width="2"/><rect x="0.5" y="7" width="11" height="8.5" rx="1" fill="#e8eef5"/></svg>
      <svg class="battery" width="28" height="13" viewBox="0 0 28 13"><rect x="0.75" y="0.75" width="24" height="11.5" rx="2" fill="none" stroke="#e8eef5" stroke-width="1.5"/><rect x="3" y="3" width="19.5" height="7" fill="#e8eef5"/><rect x="25.5" y="4" width="2.5" height="5" fill="#e8eef5"/></svg>
    </div>

    <div class="round-icon round-icon--settings" aria-label="Settings">
      <svg width="44" height="44" viewBox="0 0 44 44"><g fill="#fff"><circle cx="22" cy="22" r="13"/><g><rect x="18" y="4" width="8" height="10" rx="1.5"/><rect x="18" y="30" width="8" height="10" rx="1.5"/><rect x="4" y="18" width="10" height="8" rx="1.5"/><rect x="30" y="18" width="10" height="8" rx="1.5"/><rect x="18" y="4" width="8" height="10" rx="1.5" transform="rotate(45 22 22)"/><rect x="18" y="30" width="8" height="10" rx="1.5" transform="rotate(45 22 22)"/><rect x="4" y="18" width="10" height="8" rx="1.5" transform="rotate(45 22 22)"/><rect x="30" y="18" width="10" height="8" rx="1.5" transform="rotate(45 22 22)"/></g></g><circle cx="22" cy="22" r="5.5" fill="#4bb3ea"/></svg>
    </div>
    <div class="round-icon round-icon--info" aria-label="Information">
      <svg width="44" height="44" viewBox="0 0 44 44"><circle cx="22" cy="22" r="18" fill="none" stroke="#fff" stroke-width="4"/><circle cx="22" cy="13.5" r="3" fill="#fff"/><rect x="19.5" y="19" width="5" height="14" rx="1" fill="#fff"/></svg>
    </div>

    <div class="burst" role="img" aria-label="Burst of light rays with scattered digits circling the game name"></div>
    <div class="brand"><span class="mark"></span>QUADRIX</div>

    <div class="menu-button menu-button--single">Single Player</div>
    <div class="menu-button menu-button--multi">Multiplayer</div>
  </section>

  <section class="screen screen--bright" aria-label="Home screen, bright blue theme">
    <div class="status-bar">
      <span class="carrier">
        <svg width="18" height="12" viewBox="0 0 18 12"><rect x="0" y="9" width="3" height="3" fill="#e8eef5"/><rect x="4" y="7" width="3" height="5" fill="#e8eef5"/><rect x="8" y="5" width="3" height="7" fill="#e8eef5"/><rect x="12" y="2" width="3" height="10" fill="#e8eef5"/></svg>
        CARRIER
      </span>
      <svg class="lock" width="12" height="16" viewBox="0 0 12 16"><path d="M3 7V4.5a3 3 0 0 1 6 0V7" fill="none" stroke="#e8eef5" stroke-width="2"/><rect x="0.5" y="7" width="11" height="8.5" rx="1" fill="#e8eef5"/></svg>
      <svg class="battery" width="28" height="13" viewBox="0 0 28 13"><rect x="0.75" y="0.75" width="24" height="11.5" rx="2" fill="none" stroke="#e8eef5" stroke-width="1.5"/><rect x="3" y="3" width="19.5" height="7" fill="#e8eef5"/><rect x="25.5" y="4" width="2.5" height="5" fill="#e8eef5"/></svg>
    </div>

    <div class="round-icon round-icon--settings" aria-label="Settings">
      <svg width="44" height="44" viewBox="0 0 44 44"><g fill="#fff"><circle cx="22" cy="22" r="13"/><rect x="18" y="4" width="8" height="10" rx="1.5"/><rect x="18" y="30" width="8" height="10" rx="1.5"/><rect x="4" y="18" width="10" height="8" rx="1.5"/><rect x="30" y="18" width="10" height="8" rx="1.5"/><rect x="18" y="4" width="8" height="10" rx="1.5" transform="rotate(45 22 22)"/><rect x="18" y="30" width="8" height="10" rx="1.5" transform="rotate(45 22 22)"/><rect x="4" y="18" width="10" height="8" rx="1.5" transform="rotate(45 22 22)"/><rect x="30" y="18" width="10" height="8" rx="1.5" transform="rotate(45 22 22)"/></g><circle cx="22" cy="22" r="5.5" fill="#3a9be0"/></svg>
    </div>
    <div class="round-icon round-icon--info" aria-label="Information">
      <svg width="44" height="44" viewBox="0 0 44 44"><circle cx="22" cy="22" r="18" fill="none" stroke="#fff" stroke-width="4"/><circle cx="22" cy="13.5" r="3" fill="#fff"/><rect x="19.5" y="19" width="5" height="14" rx="1" fill="#fff"/></svg>
    </div>

    <div class="burst" role="img" aria-label="Burst of light rays with scattered digits circling the game name over a fine grid"></div>
    <div class="brand"><span class="mark"></span>QUADRIX</div>

    <div class="menu-button menu-button--single">Single Player</div>
    <div class="menu-button menu-button--multi">Multiplayer</div>
  </section>

</main>
</body>
</html>
```